Pathways to Brightmoor Land Ventures

size of the ad - 8”x 10.75" plus 0.25" bleed
I would like an ad for a magazine that will stand out and make people want to read the ad.
The ad should not be crowded and people reading the ad will be able to read the text.
I would like it to be a creative and modern-day design.
the list of topics should not be the focus of the ad.
the text is attached.
If you decide to use people in the ad then please no ladies.
please note that leave over 1 inch for the bottom of the footer

```html
<!DOCTYPE html>
<html lang="en">
<head>
<meta charset="utf-8">
<title>Real Estate Course</title>
<link href="https://fonts.googleapis.com/css2?family=Montserrat:wght@300;400;700;800;900&family=Raleway:wght@300;400;600;700&family=Roboto:wght@400&display=swap" rel="stylesheet">
<style>
  :root{
    --navy:#0e446f;
    --sky:#7ecaf2;
    --slate:#435f87;
    --backdrop:#bbbbbb;
    --white:#ffffff;
    --rule:#8a8a8a;
  }
  *{margin:0;padding:0;box-sizing:border-box}
  html,body{width:1200px;height:1200px;overflow:hidden;background:var(--backdrop)}
  .page{position:absolute;left:187px;top:49px;width:826px;height:1101px;background:var(--white);overflow:hidden}
  .course-title{position:absolute;top:58px;left:0;width:100%;text-align:center;font:900 58px/1 "Montserrat",sans-serif;color:var(--navy);letter-spacing:0.5px}
  .skyline{position:absolute;left:400px;top:150px;width:413px;height:340px;border-radius:24px;background:linear-gradient(180deg,#eef3f8 0%,#c3d6e7 30%,#7e9fc1 62%,#4f6f94 88%,#e9eef3 100%)}
  .info-card{position:absolute;left:69px;top:157px;width:351px;height:332px}
  .info-card__top{height:192px;background:var(--sky);border-top-right-radius:100px;color:var(--white);text-align:center;padding-top:22px}
  .info-card__bottom{height:140px;background:var(--slate);border-bottom-left-radius:100px;color:var(--white);text-align:center;padding-top:16px}
  .location{font:700 34px/1 "Raleway",sans-serif}
  .sessions{margin:14px auto 0;width:260px;border-top:1px dotted rgba(255,255,255,.85);border-bottom:1px dotted rgba(255,255,255,.85);padding:5px 0 6px;font:700 15.5px/1.2 "Raleway",sans-serif}
  .start-date{margin-top:7px;font:700 34px/1 "Raleway",sans-serif}
  .scholarships{margin-top:16px;font:300 16px/1 "Raleway",sans-serif}
  .early-bird{font:600 20px/1 "Raleway",sans-serif}
  .early-bird__note{margin-top:13px;font:400 16.5px/1.3 "Roboto",sans-serif}
  .program-band{position:absolute;left:0;top:509px;width:100%;height:105px;background:var(--navy);color:var(--white);text-align:center;padding-top:18px}
  .program-name{font:800 29px/1 "Montserrat",sans-serif;letter-spacing:.4px;text-transform:uppercase}
  .program-motto{margin-top:14px;font:400 21px/1 "Montserrat",sans-serif;letter-spacing:1px}
  .topics-heading{position:absolute;top:643px;left:0;width:100%;text-align:center;font:800 28px/1 "Montserrat",sans-serif;color:var(--navy)}
  .topics-heading span{font-weight:300}
  .topics{position:absolute;left:71px;top:698px;width:685px;display:grid;grid-template-columns:repeat(5,137px);grid-template-rows:146px 146px}
  .topic{text-align:center;color:var(--navy);font:700 13.5px/1.25 "Montserrat",sans-serif;letter-spacing:-0.2px;white-space:nowrap;display:flex;flex-direction:column;align-items:center}
  .topic svg{display:block;margin:0 auto 12px;width:76px;height:76px;flex:none}
  .footer-rule{position:absolute;left:0;top:988px;width:100%;border-top:1px dotted var(--rule)}
</style>
</head>
<body>
<div class="page">
  <h1 class="course-title">REAL ESTATE COURSE</h1>

  <div class="skyline" role="img" aria-label="Cluster of modern glass skyscrapers"></div>

  <div class="info-card">
    <div class="info-card__top">
      <div class="location">Larkfield</div>
      <div class="sessions">10 -Tuesday evenings sessions</div>
      <div class="start-date">Starting Feb.28</div>
      <div class="scholarships">Limited Partial Scholarships</div>
    </div>
    <div class="info-card__bottom">
      <div class="early-bird">Early Bird Special</div>
      <div class="early-bird__note">For those that started or would<br>like to go into real estate</div>
    </div>
  </div>

  <div class="program-band">
    <div class="program-name">Pathways to Brightmoor Land Ventures</div>
    <div class="program-motto">INVESTING IN KNOWLEDGE IS INVESTING IN OPPORTUNITIES.</div>
  </div>

  <h2 class="topics-heading">TOPICS: <span>PARTIAL LISTING</span></h2>

  <div class="topics">
    <div class="topic"><svg viewBox="0 0 76 76"><circle cx="38" cy="38" r="37" fill="none" stroke="#0e446f" stroke-width="1.5"/><circle cx="38" cy="38" r="33" fill="#0e446f"/><g fill="none" stroke="#fff" stroke-width="1.6"><circle cx="40" cy="34" r="9"/><path d="M40 29v5h4M18 50h8l10 4 20-8"/></g></svg>Real estate<br>investment strategies</div>
    <div class="topic"><svg viewBox="0 0 76 76"><circle cx="38" cy="38" r="37" fill="none" stroke="#0e446f" stroke-width="1.5"/><circle cx="38" cy="38" r="33" fill="#0e446f"/><g fill="none" stroke="#fff" stroke-width="1.6"><circle cx="30" cy="33" r="7"/><circle cx="40" cy="38" r="9"/><path d="M46 44l8 8"/></g></svg>Due diligence</div>
    <div class="topic"><svg viewBox="0 0 76 76"><circle cx="38" cy="38" r="37" fill="none" stroke="#0e446f" stroke-width="1.5"/><circle cx="38" cy="38" r="33" fill="#0e446f"/><g fill="none" stroke="#fff" stroke-width="1.6"><path d="M26 28h10l-3 5c8 4 8 16-2 16s-10-12-2-16z"/><circle cx="40" cy="46" r="7"/><ellipse cx="50" cy="36" rx="6" ry="2.5"/><path d="M44 36v10M56 36v10"/></g></svg>Financing</div>
    <div class="topic"><svg viewBox="0 0 76 76"><circle cx="38" cy="38" r="37" fill="none" stroke="#0e446f" stroke-width="1.5"/><circle cx="38" cy="38" r="33" fill="#0e446f"/><g fill="none" stroke="#fff" stroke-width="1.6"><rect x="27" y="21" width="22" height="34" rx="2"/><circle cx="38" cy="31" r="4"/><path d="M31 42h14M31 46h14M31 50h10"/></g></svg>Underwriting</div>
    <div class="topic"><svg viewBox="0 0 76 76"><circle cx="38" cy="38" r="37" fill="none" stroke="#0e446f" stroke-width="1.5"/><circle cx="38" cy="38" r="33" fill="#0e446f"/><g fill="none" stroke="#fff" stroke-width="1.6"><path d="M30 32l6-5 6 5v6H30zM46 24h6v14h-6M20 40h6v12h-6M26 44h10l14-4"/></g></svg>Property<br>management</div>
    <div class="topic"><svg viewBox="0 0 76 76"><circle cx="38" cy="38" r="37" fill="none" stroke="#0e446f" stroke-width="1.5"/><circle cx="38" cy="38" r="33" fill="#0e446f"/><g fill="none" stroke="#fff" stroke-width="1.6"><rect x="24" y="20" width="26" height="36"/><path d="M29 28h16M29 33h16M29 38h16M29 43h16M29 48h12M53 30l4 22"/></g></svg>Real estate<br>Legal basics</div>
    <div class="topic"><svg viewBox="0 0 76 76"><circle cx="38" cy="38" r="37" fill="none" stroke="#0e446f" stroke-width="1.5"/><circle cx="38" cy="38" r="33" fill="#0e446f"/><g fill="none" stroke="#fff" stroke-width="1.6"><path d="M24 22h20v30H24z M28 30h10M28 35h10M28 40h8"/><circle cx="48" cy="44" r="9"/><path d="M43 44l4 3 5-5"/></g></svg>Sourcing deals</div>
    <div class="topic"><svg viewBox="0 0 76 76"><circle cx="38" cy="38" r="37" fill="none" stroke="#0e446f" stroke-width="1.5"/><circle cx="38" cy="38" r="33" fill="#0e446f"/><g fill="none" stroke="#fff" stroke-width="1.6"><rect x="33" y="31" width="10" height="14"/><path d="M38 27v-7M38 49v7M29 38h-7M47 38h7M31 31l-5-5M45 31l5-5M31 45l-5 5M45 45l5 5"/></g></svg>Syndication</div>
    <div class="topic"><svg viewBox="0 0 76 76"><circle cx="38" cy="38" r="37" fill="none" stroke="#0e446f" stroke-width="1.5"/><circle cx="38" cy="38" r="33" fill="#0e446f"/><g fill="none" stroke="#fff" stroke-width="1.6"><circle cx="30" cy="27" r="3"/><circle cx="38" cy="26" r="3"/><circle cx="46" cy="27" r="3"/><path d="M22 42l8-6 8 4 8-4 8 6-10 8-6-4-6 4z"/></g></svg>Dealing<br>with brokers</div>
    <div class="topic"><svg viewBox="0 0 76 76"><circle cx="38" cy="38" r="37" fill="none" stroke="#0e446f" stroke-width="1.5"/><circle cx="38" cy="38" r="33" fill="#0e446f"/><g fill="none" stroke="#fff" stroke-width="1.6"><circle cx="44" cy="30" r="10"/><path d="M40 35l8-10"/><ellipse cx="30" cy="44" rx="7" ry="2.5"/><path d="M23 44v9M37 44v9"/><ellipse cx="30" cy="53" rx="7" ry="2.5"/></g></svg>Tax fundamentals</div>
  </div>

  <div class="footer-rule"></div>
</div>
</body>
</html>
```